Family Medicine Clinic Needs Mailchimp Newsletter Template

Looking for a responsive mailchimp template that matches the theme and overall look/feel of our website brookvaleclinic.com.

I'm looking for a professional, clean, simple, minimalist, bold design.
Colors would ideally be greens and blues, cool tones, muted colors, or graytones.

See attached word document for content for the upcoming newsletter

Can see prior newsletter content here:
http://brookvaleclinic.com/ourresources/newsletter-archive/

I have attached a copy of our brochure to see a sample of what we offer

The desired newsletter title would be:
The Brook Note
Looking for a great banner for that

Looking for basically 1 main photo area per text area for future templates

Under September is Spine Focus Season want links to our different services I mention

Under the videos section would like a video gallery of sorts that have links to the videos

Lumaderm image ad needs to be redone

Would like a button to take to schedule an appointment and patient portal
Easily visible phone number
Would like to have several sections with buttons to find out more

Would like feedback question at bottom
Rated 7-10 would forward to
https://lnkvo.net/qX8pZa

1-6 would send email to us

Reason: I have now guaranteed payment so I am giving a few more days for those designers that still want to submit a design

Clinic

Coded - Design and coding required

```html
<!DOCTYPE html>
<html lang="en">
<head>
<meta charset="utf-8">
<title>The Brook Note — Brookvale Family Medicine</title>
<link href="https://fonts.googleapis.com/css2?family=Roboto:wght@400;500;700;900&family=Roboto+Condensed:wght@700&display=swap" rel="stylesheet">
<style>
:root{
  --blue:#2a9bd8;
  --blue-dark:#1f7fb6;
  --green:#8dc21f;
  --green-dark:#76a816;
  --ink:#2b2b2b;
  --icon:#3a3a3a;
  --text:#555;
  --grey-bg:#efefef;
  --footer:#2d2d2d;
  --white:#fff;
}
*{box-sizing:border-box;margin:0;padding:0}
html,body{width:1200px;height:3689px;overflow:hidden;background:var(--white)}
body{position:relative;font-family:'Roboto',Arial,sans-serif;color:var(--ink)}
.abs{position:absolute}
.heading{font-family:'Roboto Condensed','Roboto',sans-serif;font-weight:700;text-transform:uppercase;text-align:center;letter-spacing:.5px}
.btn{position:absolute;display:flex;align-items:center;justify-content:center;gap:10px;border-radius:40px;font-weight:700;font-size:14px;text-transform:uppercase;letter-spacing:.5px;color:var(--white);background:var(--green);box-shadow:0 3px 0 var(--green-dark)}
.btn-white{background:var(--white);color:var(--ink);box-shadow:0 3px 0 rgba(0,0,0,.15)}

/* header */
.site-header{position:absolute;left:0;top:0;width:1200px;height:140px;background:var(--white)}
.brand{position:absolute;left:74px;top:28px;display:flex;align-items:center;gap:16px}
.brand-dot{width:60px;height:60px;border-radius:50%;background:var(--green)}
.brand-name{font-weight:700;color:var(--blue);font-size:40px;line-height:1.05}
.brand-name small{display:block;font-size:17px;letter-spacing:3px;font-weight:700}
.phone{position:absolute;left:745px;top:14px;display:flex;align-items:center;gap:10px;font-weight:700;font-size:22px;color:var(--blue)}
.portal{left:947px;top:10px;width:179px;height:39px;font-size:13px}
.schedule{left:811px;top:76px;width:315px;height:54px;font-size:16px}

/* hero */
.hero{position:absolute;left:0;top:140px;width:1200px;height:520px;background:
  radial-gradient(ellipse 220px 260px at 130px 250px,#e7c3a4 0%,rgba(231,195,164,0) 100%),
  radial-gradient(ellipse 260px 280px at 520px 300px,#f3d7bf 0%,rgba(243,215,191,0) 100%),
  radial-gradient(ellipse 240px 260px at 860px 240px,#eac7a8 0%,rgba(234,199,168,0) 100%),
  radial-gradient(ellipse 200px 260px at 1120px 280px,#f0e2d4 0%,rgba(240,226,212,0) 100%),
  linear-gradient(180deg,#b9d4c4 0%,#cfb79a 55%,#a98e76 100%)}
.hero-title{position:absolute;left:0;top:364px;width:1200px;font-size:72px;color:var(--blue);text-shadow:0 0 18px rgba(255,255,255,.9)}

/* feature */
.feature-panel{position:absolute;left:0;top:606px;width:344px;height:430px;background:var(--green)}
.feature-panel h2{position:absolute;left:82px;top:140px;width:250px;font-family:'Roboto',sans-serif;font-weight:900;color:var(--white);font-size:28px;line-height:1.22;text-transform:uppercase}
.feature-panel h2 .big{display:block;font-size:36px;color:var(--ink)}
.know-title{position:absolute;left:405px;top:716px;font-size:27px;font-weight:700;color:var(--ink);text-transform:uppercase}
.fact{position:absolute;top:772px;width:330px;display:flex;gap:16px;font-size:14px;line-height:1.8;color:var(--text)}
.fact svg{flex:none;margin-top:2px}

/* services */
.services-title{position:absolute;left:0;top:1055px;width:1200px;font-size:30px;color:var(--white)}
.service{position:absolute;width:270px;text-align:center;color:var(--white);font-size:18px;font-weight:500;line-height:1.3}
.service .icon{display:flex;align-items:center;justify-content:center;width:98px;height:98px;border-radius:50%;background:var(--white);margin:0 auto 16px;box-shadow:0 3px 0 rgba(0,0,0,.12);color:var(--icon)}
.service .icon svg{width:52px;height:52px;fill:none;stroke:currentColor;stroke-width:3;stroke-linecap:round;stroke-linejoin:round}
.divider-v{position:absolute;width:1px;background:rgba(255,255,255,.25)}
.divider-h{position:absolute;height:1px;background:rgba(255,255,255,.25)}

/* video */
.section-title{position:absolute;left:0;width:1200px;font-size:30px;color:var(--ink)}
.video{position:absolute;border:2px solid #ddd;background:
  radial-gradient(ellipse 40% 55% at 45% 65%,#5a4a42 0%,rgba(90,74,66,0) 100%),
  linear-gradient(90deg,#c9c5b8 0%,#ece8de 45%,#d6d2c6 70%,#b9c3b0 100%)}
.video.blue{background:radial-gradient(ellipse 35% 60% at 45% 70%,#3f5f9a 0%,rgba(63,95,154,0) 100%),linear-gradient(135deg,#7d8c8f,#c9c6ba)}
.play{position:absolute;left:50%;top:50%;transform:translate(-50%,-50%);background:var(--white);border-radius:10px;display:flex;align-items:center;justify-content:center}
.player-bar{position:absolute;left:0;right:0;bottom:0;height:26px;background:rgba(0,0,0,.75)}

/* gallery */
.gallery{position:absolute;left:0;top:2373px;width:1200px;height:560px;background:var(--grey-bg)}
.shot{position:absolute;border:3px solid var(--white);background:
  radial-gradient(ellipse 60% 45% at 50% 45%,#f2ddd0 0%,rgba(242,221,208,0) 100%),
  linear-gradient(135deg,#d7ae95 0%,#ecd2c1 50%,#c49680 100%)}
.shot span{position:absolute;left:12px;bottom:10px;font-size:12px;font-weight:700;font-style:italic;color:var(--white);text-transform:uppercase}

/* feedback */
.feedback-title{position:absolute;left:0;top:2980px;width:1200px;font-size:30px;color:var(--white)}
.review{position:absolute;top:3056px;width:330px;text-align:center;color:var(--ink)}
.stars{font-size:20px;letter-spacing:5px}
.score{font-weight:700;font-size:15px;margin:4px 0 8px}
.review p{font-size:14px;line-height:1.7}

/* footer */
.footer-brand{position:absolute;left:0;top:3418px;width:1200px;display:flex;justify-content:center;align-items:center;gap:14px}
.copyright{position:absolute;left:0;top:3558px;width:1200px;text-align:center;color:#8a8a8a;font-size:13px}
.socials{position:absolute;left:0;top:3592px;width:1200px;display:flex;justify-content:center;gap:22px}
.socials span{width:26px;height:26px;border-radius:4px;background:#9a9a9a}
</style>
</head>
<body>

<header class="site-header">
  <div class="brand"><span class="brand-dot"></span><div class="brand-name">Brookvale<small>FAMILY MEDICINE</small></div></div>
  <div class="phone">
    <svg width="20" height="20" viewBox="0 0 24 24"><path fill="currentColor" d="M6.6 10.8a15 15 0 0 0 6.6 6.6l2.2-2.2a1 1 0 0 1 1-.25 11.4 11.4 0 0 0 3.6.57 1 1 0 0 1 1 1V20a1 1 0 0 1-1 1A17 17 0 0 1 3 4a1 1 0 0 1 1-1h3.5a1 1 0 0 1 1 1c0 1.25.2 2.45.57 3.57a1 1 0 0 1-.25 1z"/></svg>
    (555) 014-2290
  </div>
  <a class="btn btn-white portal">Patient Portal</a>
  <a class="btn schedule">
    <svg width="18" height="18" viewBox="0 0 24 24"><rect x="3" y="5" width="18" height="16" rx="2" fill="none" stroke="#fff" stroke-width="2"/><path d="M3 10h18M8 3v4M16 3v4" stroke="#fff" stroke-width="2"/></svg>
    Schedule an Appointment
  </a>
</header>

<section class="hero" role="img" aria-label="Photo of a smiling multi-generation family outdoors"></section>
<svg class="abs" style="left:0;top:560px" width="1200" height="110" viewBox="0 0 1200 110"><path d="M0 110 L0 70 Q600 -40 1200 50 L1200 110 Z" fill="#fff"/></svg>
<h1 class="hero-title heading">The Brook Note</h1>

<section class="feature">
  <div class="feature-panel"><h2>September is <span class="big">Spine Focus Season</span></h2></div>
  <svg class="abs" style="left:344px;top:800px" width="22" height="44" viewBox="0 0 22 44"><path d="M0 0 L22 22 L0 44 Z" fill="#8dc21f"/></svg>
  <h2 class="know-title">What you need to know</h2>
  <div class="fact" style="left:405px">
    <svg width="26" height="26" viewBox="0 0 26 26"><circle cx="13" cy="13" r="11" fill="none" stroke="#8dc21f" stroke-width="3"/><path d="M8 13l4 4 7-8" fill="none" stroke="#8dc21f" stroke-width="3"/></svg>
    <span>Nearly 100 million Americans experience chronic pain more than those who have diabetes, heart disease and cancer combined.</span>
  </div>
  <div class="fact" style="left:782px">
    <svg width="26" height="26" viewBox="0 0 26 26"><circle cx="13" cy="13" r="11" fill="none" stroke="#8dc21f" stroke-width="3"/><path d="M8 13l4 4 7-8" fill="none" stroke="#8dc21f" stroke-width="3"/></svg>
    <span>Nearly 100 million Americans experience chronic pain more than those who have diabetes, heart disease and cancer combined.</span>
  </div>
  <a class="btn" style="left:405px;top:878px;width:182px;height:48px">Find out more &raquo;</a>
</section>

<section class="services">
  <svg class="abs" style="left:0;top:980px" width="1200" height="845" viewBox="0 0 1200 845" preserveAspectRatio="none"><path d="M344 60 Q800 -40 1200 40 L1200 740 Q600 880 0 760 L0 60 Z" fill="#2a9bd8"/></svg>
  <h2 class="services-title heading">Our Services</h2>
  <div class="divider-v" style="left:330px;top:1130px;height:560px"></div>
  <div class="divider-v" style="left:600px;top:1130px;height:560px"></div>
  <div class="divider-v" style="left:870px;top:1130px;height:560px"></div>
  <div class="divider-h" style="left:74px;top:1308px;width:1052px"></div>
  <div class="divider-h" style="left:74px;top:1495px;width:1052px"></div>

  <div class="service" style="left:60px;top:1135px"><span class="icon"><svg viewBox="0 0 48 48"><circle cx="24" cy="24" r="19"/><path d="M20 12h8v8h8v8h-8v8h-8v-8h-8v-8h8z"/></svg></span>Integrative Family<br>Medicine</div>
  <div class="service" style="left:330px;top:1135px"><span class="icon"><svg viewBox="0 0 48 48"><circle cx="24" cy="19" r="12"/><path d="M24 31v12M17 43h14M24 24l-5-5M24 27l6-6"/></svg></span>Functional Medicine</div>
  <div class="service" style="left:600px;top:1135px"><span class="icon"><svg viewBox="0 0 48 48"><path d="M24 16c-5-5-15-3-15 9 0 11 8 19 15 15 7 4 15-4 15-15 0-12-10-14-15-9z"/><path d="M24 16c0-5 2-8 6-9"/></svg></span>Nutrition</div>
  <div class="service" style="left:870px;top:1135px"><span class="icon"><svg viewBox="0 0 48 48"><rect x="7" y="9" width="34" height="32" rx="6"/><path d="M15 20a9 9 0 0 1 18 0z"/><path d="M24 20l3-5"/></svg></span>Weight Loss</div>

  <div class="service" style="left:60px;top:1322px"><span class="icon"><svg viewBox="0 0 48 48"><rect x="18" y="5" width="12" height="7" rx="3"/><rect x="17" y="15" width="14" height="7" rx="3"/><rect x="16" y="25" width="16" height="7" rx="3"/><rect x="15" y="35" width="18" height="8" rx="3"/></svg></span>Osteopathic<br>Manipulation</div>
  <div class="service" style="left:330px;top:1322px"><span class="icon"><svg viewBox="0 0 48 48"><path d="M6 34h36M10 34v8M38 34v8"/><path d="M16 10v20M24 8v22M32 10v20"/><circle cx="16" cy="8" r="2"/><circle cx="24" cy="6" r="2"/><circle cx="32" cy="8" r="2"/></svg></span>Acupuncture</div>
  <div class="service" style="left:600px;top:1322px"><span class="icon"><svg viewBox="0 0 48 48"><circle cx="18" cy="26" r="9"/><path d="M18 35v9M14 40h8"/><circle cx="30" cy="18" r="9"/><path d="M36 12l7-7M37 5h6v6"/></svg></span>Bio-Identical Hormone<br>Replacement</div>
  <div class="service" style="left:870px;top:1322px"><span class="icon"><svg viewBox="0 0 48 48"><path d="M19 6h10M21 6v13L10 39a3 3 0 0 0 3 4h22a3 3 0 0 0 3-4L27 19V6"/><path d="M14 32h20"/></svg></span>Labs</div>

  <div class="service" style="left:60px;top:1509px"><span class="icon"><svg viewBox="0 0 48 48"><rect x="4" y="12" width="40" height="24" rx="3"/><path d="M8 25h8l3-7 5 14 4-10 2 3h10"/></svg></span>CIMT</div>
  <div class="service" style="left:330px;top:1509px"><span class="icon"><svg viewBox="0 0 48 48"><path d="M24 22c-4-5-6-9-6-12a6 6 0 0 1 12 0c0 3-2 7-6 12zM24 22l-10 22M24 22l10 22"/></svg></span>Breast<br>Thermography</div>
  <div class="service" style="left:600px;top:1509px"><span class="icon"><svg viewBox="0 0 48 48"><path d="M34 6l8 8M38 10l-6 6M32 12L14 30l4 4 18-18M14 30l-8 8v4h4l8-8M20 20l3 3M24 16l3 3"/></svg></span>Prolo/PRP/Stem<br>Cell Injections</div>
  <div class="service" style="left:870px;top:1509px"><span class="icon"><svg viewBox="0 0 48 48"><path d="M24 6C18 15 12 22 12 30a12 12 0 0 0 24 0c0-8-6-15-12-24z"/><path d="M18 31a6 6 0 0 0 6 6"/></svg></span>Allergy Testing</div>

  <a class="btn" style="left:510px;top:1708px;width:182px;height:48px">Find out more &raquo;</a>
</section>

<section class="videos">
  <h2 class="section-title heading" style="top:1866px">Video Gallery</h2>
  <div class="video" style="left:74px;top:1930px;width:602px;height:389px" role="img" aria-label="Video still of a clinician speaking in an exam room">
    <div class="play" style="width:92px;height:66px"><svg width="32" height="36" viewBox="0 0 32 36"><path d="M2 2 L30 18 L2 34 Z" fill="#444"/></svg></div>
    <div class="player-bar"></div>
  </div>
  <div class="video blue" style="left:703px;top:1930px;width:204px;height:148px" role="img" aria-label="Video thumbnail"><div class="play" style="width:40px;height:30px"><svg width="14" height="16" viewBox="0 0 32 36"><path d="M2 2 L30 18 L2 34 Z" fill="#444"/></svg></div></div>
  <div class="video" style="left:925px;top:1930px;width:201px;height:148px" role="img" aria-label="Video thumbnail"><div class="play" style="width:40px;height:30px"><svg width="14" height="16" viewBox="0 0 32 36"><path d="M2 2 L30 18 L2 34 Z" fill="#444"/></svg></div></div>
  <div class="video blue" style="left:703px;top:2095px;width:204px;height:148px" role="img" aria-label="Video thumbnail"><div class="play" style="width:40px;height:30px"><svg width="14" height="16" viewBox="0 0 32 36"><path d="M2 2 L30 18 L2 34 Z" fill="#444"/></svg></div></div>
  <div class="video blue" style="left:925px;top:2095px;width:201px;height:148px" role="img" aria-label="Video thumbnail"><div class="play" style="width:40px;height:30px"><svg width="14" height="16" viewBox="0 0 32 36"><path d="M2 2 L30 18 L2 34 Z" fill="#444"/></svg></div></div>
  <a class="btn" style="left:825px;top:2268px;width:182px;height:48px">Find out more &raquo;</a>
</section>

<section class="gallery">
  <h2 class="section-title heading" style="top:40px">Lumaderm Gallery</h2>
  <div class="shot" style="left:74px;top:103px;width:201px;height:145px" role="img" aria-label="Before treatment close-up"><span>Before</span></div>
  <div class="shot" style="left:295px;top:103px;width:202px;height:145px" role="img" aria-label="After treatment close-up"><span>After</span></div>
  <div class="shot" style="left:74px;top:268px;width:201px;height:145px" role="img" aria-label="Before treatment close-up"><span>Before</span></div>
  <div class="shot" style="left:295px;top:268px;width:202px;height:145px" role="img" aria-label="After treatment close-up"><span>After</span></div>
  <div class="shot" style="left:529px;top:103px;width:282px;height:310px" role="img" aria-label="Before treatment portrait"><span>Before</span></div>
  <div class="shot" style="left:841px;top:103px;width:285px;height:310px" role="img" aria-label="After treatment portrait"><span>After</span></div>
  <a class="btn" style="left:510px;top:442px;width:182px;height:48px">Find out more &raquo;</a>
</section>

<section class="feedback">
  <svg class="abs" style="left:0;top:2921px" width="1200" height="450" viewBox="0 0 1200 450" preserveAspectRatio="none"><path d="M0 0 L1200 0 L1200 440 Q600 330 0 420 Z" fill="#8dc21f"/></svg>
  <h2 class="feedback-title heading">Feedback Question</h2>
  <div class="review" style="left:76px"><div class="stars">★★★★★★★</div><div class="score">7/10</div><p>Vestibulum vel metus sit amet turpis bibendum tincidunt vel sit amet quam. Pellentesque habitant morbi tristique senectus et netus et malesuada fames ac turpis egestas.</p></div>
  <div class="review" style="left:435px"><div class="stars">★★★★★★★</div><div class="score">7/10</div><p>Vestibulum vel metus sit amet turpis bibendum tincidunt vel sit amet quam. Pellentesque habitant morbi tristique senectus et netus et malesuada fames ac turpis egestas.</p></div>
  <div class="review" style="left:794px"><div class="stars">★★★★★★★</div><div class="score">7/10</div><p>Vestibulum vel metus sit amet turpis bibendum tincidunt vel sit amet quam. Pellentesque habitant morbi tristique senectus et netus et malesuada fames ac turpis egestas.</p></div>
  <a class="btn btn-white" style="left:510px;top:3260px;width:182px;height:46px">Find out more &raquo;</a>
</section>

<footer class="site-footer">
  <svg class="abs" style="left:0;top:3460px" width="1200" height="229" viewBox="0 0 1200 229" preserveAspectRatio="none"><path d="M0 50 Q600 -30 1200 60 L1200 229 L0 229 Z" fill="#2d2d2d"/></svg>
  <div class="footer-brand"><span class="brand-dot" style="width:46px;height:46px"></span><div class="brand-name" style="font-size:30px">Brookvale<small style="font-size:15px">FAMILY MEDICINE</small></div></div>
  <p class="copyright">Copyright © 2017 Brookvale Family Medicine. All rights reserved.</p>
  <div class="socials" aria-label="Social links"><span></span><span></span><span></span><span></span></div>
</footer>

</body>
</html>
```